Two Bodyguards

Cover for a book in French language:
- Author: Mathieu Ferrand-Lacoste
- Title: Cold suspects rarely ever smile back
- Publisher (at the bottom of the page): Editions Vernaille
Key Words:
- a rich man died recently, it looks like a murder. He has been found in his luxury apartment.
- Two Body Guards: one is elegant, the other a bit fat.
- two pretty women.
- Inheritance (wealth)
Size of the cover: 14 x 20.5 cm (+ bleed area)
Please note that the title should remain in English: "Suspects rarely ever smile back".
By the way the title doesn't mean anything. It's just a joke.
Thrillers' reader

```html
<!DOCTYPE html>
<html lang="en">
<head>
<meta charset="utf-8">
<title>Suspects rarely ever smile back — Mathieu Ferrand-Lacoste</title>
<link rel="stylesheet" href="https://fonts.googleapis.com/css2?family=Cinzel:wght@400&family=Creepster&family=Oswald:wght@600&display=swap">
<style>
  :root {
    --sky-light: #8fa8a2;
    --sky-mid: #3f5a5a;
    --sky-dark: #16262a;
    --facade: #2b3a3e;
    --facade-deep: #0f1a1d;
    --title-yellow: #ffec00;
    --title-shadow: #1a1f12;
    --ink-white: #f4f4f2;
  }
  html, body {
    margin: 0;
    padding: 0;
    width: 819px;
    height: 1200px;
    overflow: hidden;
    background: var(--facade-deep);
  }
  .cover {
    position: relative;
    width: 819px;
    height: 1200px;
    overflow: hidden;
  }
  .cover-art {
    position: absolute;
    inset: 0;
    display: block;
  }
  .author {
    position: absolute;
    top: 56px;
    left: 0;
    width: 100%;
    margin: 0;
    text-align: center;
    font-family: "Cinzel", serif;
    font-weight: 400;
    font-size: 34px;
    letter-spacing: 5px;
    color: var(--ink-white);
  }
  .title {
    position: absolute;
    top: 500px;
    left: 160px;
    width: 520px;
    margin: 0;
    font-family: "Creepster", cursive;
    font-weight: 400;
    font-size: 112px;
    line-height: 100px;
    color: var(--title-yellow);
    text-transform: uppercase;
    text-shadow: 5px 5px 0 var(--title-shadow);
    transform: rotate(-2deg);
  }
  .title-line {
    display: block;
    white-space: nowrap;
  }
  .title-line--1 { padding-left: 180px; }
  .title-line--2 { padding-left: 20px; }
  .title-line--3 { padding-left: 10px; }
  .title-line--4 { padding-left: 0; }
  .title-line--5 { padding-left: 40px; }
  .publisher {
    position: absolute;
    top: 1100px;
    left: 0;
    width: 100%;
    margin: 0;
    text-align: center;
    font-family: "Oswald", sans-serif;
    font-weight: 600;
    font-size: 25px;
    letter-spacing: 0.5px;
    color: var(--ink-white);
    text-transform: uppercase;
  }
</style>
</head>
<body>
  <main class="cover">
    <svg class="cover-art" width="819" height="1200" viewBox="0 0 819 1200" role="img" aria-label="Photograph of a dark, grand Haussmann-style apartment building under a stormy green-grey sky">
      <defs>
        <radialGradient id="sky" cx="0.35" cy="0.3" r="0.8">
          <stop offset="0" stop-color="var(--sky-light)"/>
          <stop offset="0.45" stop-color="var(--sky-mid)"/>
          <stop offset="1" stop-color="var(--sky-dark)"/>
        </radialGradient>
        <linearGradient id="building" x1="0" y1="0" x2="0" y2="1">
          <stop offset="0" stop-color="var(--facade)"/>
          <stop offset="0.6" stop-color="#1e2b2e"/>
          <stop offset="1" stop-color="var(--facade-deep)"/>
        </linearGradient>
      </defs>
      <rect width="819" height="1200" fill="url(#sky)"/>
      <path d="M0 640 L60 610 L110 520 L200 440 L280 360 L380 300 L500 230 L600 300 L700 370 L760 450 L819 460 L819 1200 L0 1200 Z" fill="url(#building)"/>
    </svg>

    <h2 class="author">Mathieu Ferrand-Lacoste</h2>

    <h1 class="title">
      <span class="title-line title-line--1">Suspects</span>
      <span class="title-line title-line--2">rarely</span>
      <span class="title-line title-line--3">ever smile</span>
      <span class="title-line title-line--5">back</span>
    </h1>

    <p class="publisher">Editions Vernaille</p>
  </main>
</body>
</html>
```